FLYER POSTCARD ADVERT FOR GARNET QUARTER

OUR COMPANY NAME IS TOLVEK DESIGNS.

WE NEED TO MAKE A POSTCARD FRONT AND BACK TO HAND OUT AND MAIL TO LOCAL JEWELERS DESCRIBING OUR WEDDING RING MANUFACTURING AND FINISHING SERVICES.
KEY POINTS WE WOULD LIKE LISTED:

FAST AND RELIABLE CONTRACTORS THAT ARE IN THE WEDDING RING INDUSTRY SINCE 1979

WE OFFER:
SWISS CUTTING
BASIC TO COMPLEX FINISHES AND DESIGNS
HAND CHASING/EMBOSSING AND ENGRAVING
LASER ENGRAVING
DIAMOND SETTING

CUTTING AND FINISHING AS LOW AS $10 PER PIECE

10K - 14K - 18K - PLATINUM - PALLADIUM - .935 SILVER
VOLUME AND SPECIAL ORDERS ACCEPTED
NO MINIMUMS

EMAIL : INFO@TOLVEKDESIGNS.EXAMPLE
TEL: 555 - 314- 9072

Target Market(s)

WHOLESALE JEWELERS

Industry/Entity Type

Jewelry

Font styles to use
Serif

Colors

Designer to choose colors to be used in the design.

Requirements
Must have
• OUR LOGO, WEVE ATTACHED BOTH WHITE AND BLACK BACKGROUND TO USE DEPENDING ON THE COLOR SCHEME.
• ALSO NEEDS THESE KEY POINTS LISTED TOO:
• FAST AND RELIABLE CONTRACTORS AND MANUFACTURERS SERVICING THE WEDDING RING INDUSTRY SINCE 1979
• WE OFFER:
• SWISS CUTTING
• BASIC TO COMPLEX FINISHES AND DESIGNS
• HAND CHASING/EMBOSSING AND ENGRAVING
• LASER ENGRAVING
• DIAMOND SETTING
• CUTTING AND FINISHING AS LOW AS $10 PER PIECE
• 10K - 14K - 18K - PLATINUM - PALLADIUM - .935 SILVER
• VOLUME AND SPECIAL ORDERS ACCEPTED
• NO MINIMUMS
• EMAIL : INFO@TOLVEKDESIGNS.EXAMPLE
• TEL: 555 - 314- 9072
Should not have
• WE DONT MIND COLOR, BUT WE DONT WANT AN EXPLOSION OF COLORS EITHER. WE WOULD LIKE IT TO BE EASY ON THE EYE.

```html
<!DOCTYPE html>
<html lang="en">
<head>
<meta charset="utf-8">
<title>Tolvek Designs – Postcard</title>
<link href="https://fonts.googleapis.com/css2?family=Cinzel:wght@400&family=Lato:wght@300;400;700&display=swap" rel="stylesheet">
<style>
  :root{
    --backdrop:#41444b;
    --card:#ffffff;
    --gold:#e6a817;
    --gold-pale:#d9c79a;
    --gold-line:#f3e4b8;
    --ink:#2f2f2f;
    --grey:#7b7b7b;
    --rule:#d2d2d2;
  }
  *{box-sizing:border-box;margin:0;padding:0}
  html,body{width:950px;height:1200px;overflow:hidden;background:var(--backdrop);font-family:"Lato",sans-serif}
  .card{position:absolute;left:84px;width:802px;height:526px;background:var(--card);overflow:hidden}
  .card--front{top:43px}
  .card--back{top:596px}

  .photo{position:absolute}
  .photo--hero{left:0;top:0;width:468px;height:440px;
    background:radial-gradient(ellipse at 35% 35%,#f1d873 0%,#d9b53c 35%,#c9cbce 60%,#ffffff 82%)}
  .photo--small{border-radius:40%}
  .photo--gold{background:radial-gradient(ellipse at center,#e8c85a 0%,#d7b54a 55%,#ffffff 100%)}
  .photo--silver{background:radial-gradient(ellipse at center,#d5d7da 0%,#b9bcc0 55%,#ffffff 100%)}

  .brand{position:absolute;display:flex;flex-direction:column;align-items:center;
    font-family:"Cinzel",serif;font-weight:400;color:var(--gold);text-align:center}
  .brand__mark{display:block;border-radius:50%;background:var(--gold)}
  .brand__name{display:block;white-space:nowrap}
  .brand__sub{display:block;white-space:nowrap}

  .card--front .brand{left:572px;top:336px;width:190px}
  .card--front .brand__mark{width:40px;height:40px;margin-bottom:30px}
  .card--front .brand__name{font-size:40px;line-height:40px;letter-spacing:1px}
  .card--front .brand__sub{font-size:12px;line-height:14px;margin-top:2px;letter-spacing:21px;margin-right:-21px}

  .card--back .brand{left:386px;top:40px;width:142px}
  .card--back .brand__mark{width:36px;height:36px;margin-bottom:34px}
  .card--back .brand__name{font-size:30px;line-height:30px;letter-spacing:1px}
  .card--back .brand__sub{font-size:10px;line-height:12px;margin-top:2px;letter-spacing:15px;margin-right:-15px}

  .tagline{position:absolute;left:45px;top:476px;font-size:17.5px;line-height:20px;font-weight:300;color:var(--grey);white-space:nowrap}

  .contact{position:absolute;left:51px;top:112px;font-size:18px;font-weight:700;color:var(--grey);line-height:23px}
  .offer__title{position:absolute;left:88px;top:202px;font-size:34px;line-height:40px;font-weight:300;color:var(--gold)}
  .offer__list{position:absolute;left:85px;top:252px;list-style:none;font-size:16px;font-weight:300;line-height:20px}
  .offer__list li{color:var(--ink)}
  .offer__list li:nth-child(odd){color:var(--gold-pale)}

  .divider{position:absolute;left:461px;top:160px;width:3px;height:308px;
    background:linear-gradient(to bottom,var(--gold-line),#f0e6cc 60%,rgba(255,255,255,0))}
  .stamp{position:absolute;left:656px;top:35px;width:104px;height:104px;border:3px solid var(--gold-line)}
  .address-line{position:absolute;left:492px;width:268px;height:2px;
    background:linear-gradient(to right,rgba(210,210,210,0),var(--rule) 20%,var(--rule) 80%,rgba(210,210,210,0))}
</style>
</head>
<body>
  <section class="card card--front">
    <div class="photo photo--hero" role="img" aria-label="Photo of interlocked gold and white-gold wedding bands"></div>
    <div class="brand">
      <span class="brand__mark"></span>
      <span class="brand__name">TOLVEK</span>
      <span class="brand__sub">DESIGNS</span>
    </div>
    <p class="tagline">Fast and reliable contractors and manufacturers servicing the wedding ring industry since 1979</p>
  </section>

  <section class="card card--back">
    <div class="photo photo--small photo--gold" style="left:32px;top:-10px;width:116px;height:110px" role="img" aria-label="Hammered-finish gold wedding band"></div>
    <div class="photo photo--small photo--silver" style="left:244px;top:-10px;width:124px;height:100px" role="img" aria-label="White-gold band with milgrain edges"></div>
    <div class="photo photo--small photo--silver" style="left:-20px;top:200px;width:92px;height:156px" role="img" aria-label="Hand-engraved white-gold band"></div>
    <div class="photo photo--small photo--silver" style="left:36px;top:444px;width:120px;height:110px" role="img" aria-label="Diamond-set white-gold band"></div>
    <div class="photo photo--small photo--gold" style="left:248px;top:452px;width:136px;height:100px" role="img" aria-label="Satin-finish gold band"></div>

    <div class="contact">
      <p>Marlow Bay City, NY, United States</p>
      <p>Email : info@tolvekdesigns.example</p>
      <p>Tel: 555 - 314- 9072</p>
    </div>

    <h2 class="offer__title">We offer:</h2>
    <ul class="offer__list">
      <li>- Swiss cutting</li>
      <li>- basic to complex finishes and designs</li>
      <li>- hand chasing/embossing and engraving</li>
      <li>- laser engraving</li>
      <li>- diamond setting</li>
      <li>- cutting and finishing as low as $10 per piece</li>
      <li>- 10k - 14k - 18k - platinum - palladium - .935 silver</li>
      <li>- volume and special orders accepted</li>
      <li>- no minimums</li>
    </ul>

    <div class="brand">
      <span class="brand__mark"></span>
      <span class="brand__name">TOLVEK</span>
      <span class="brand__sub">DESIGNS</span>
    </div>

    <div class="divider"></div>
    <div class="stamp"></div>
    <div class="address-line" style="top:249px"></div>
    <div class="address-line" style="top:296px"></div>
    <div class="address-line" style="top:344px"></div>
    <div class="address-line" style="top:394px"></div>
  </section>
</body>
</html>
```